Northern Tempest Informational Sheet

I need a one page informational sheet (advertisement) for a horse called Northern Tempest. It should have the name Northern Tempest and the content below. It needs to be eye-catching. I have attached 3 examples of what these advertisements look like so it's easier to create. I've also attached 2 pictures of the horse which should both be used in the advertisement.

Here are the bullet points:

- Son of Distant Harbor with total progeny earnings over 13 million dollars
- Ranks among West Virginia top 3 active sires by progeny earnings 2019
- In 9 crops of racing age, has sired 200 winners from 275 starters
- Sired Don Marbellino who earned over $800k racing from age 2 to 7.
- Won 3 of 4 lifetime starts

stands at stud for $1000 at Ashgrove Farm near Charles Town
Call Dwight Kessler - (304) 555-0193

Target Market(s)

Thoroughbred racing people interested in breeding

Requirements
Must have
• Unique and creative. The name of the horse Northern Tempest should be clear and bold, the picture should also be prominent.
Should not have
• Cartoon like, whimsical

```html
<!DOCTYPE html>
<html lang="en">
<head>
<meta charset="utf-8">
<title>Northern Tempest – Stallion Sheet</title>
<link href="https://fonts.googleapis.com/css2?family=Cinzel:wght@700&family=Josefin+Sans:wght@300&family=Cabin:wght@400&display=swap" rel="stylesheet">
<style>
  :root {
    --bg: #240b05;
    --tan: #c2a284;
    --tan-light: #d8c3ad;
    --text: #eadbd0;
    --gold: #e3b532;
    --gold-dark: #b07f12;
    --badge-core: #141010;
    --horse-dark: #5a2410;
    --horse-mid: #9a4a22;
    --yard: #5b6170;
  }
  * { margin: 0; padding: 0; box-sizing: border-box; }
  html, body { width: 849px; height: 1200px; overflow: hidden; background: var(--bg); }
  .sheet { position: relative; width: 849px; height: 1200px; background: var(--bg); overflow: hidden; font-family: "Cabin", sans-serif; }
  .sweep { position: absolute; inset: 0; }
  .title-frame { position: absolute; left: 212px; top: 31px; width: 607px; height: 339px; border: 3px solid var(--tan); }
  .photo-mount { position: absolute; left: 28px; top: 62px; width: 376px; height: 278px; background: var(--tan); padding: 8px 9px; }
  .photo-standing { width: 100%; height: 100%; background: linear-gradient(180deg, #c9c3bc 0%, #8e7a6a 40%, var(--horse-mid) 55%, var(--yard) 85%); }
  .horse-name { position: absolute; left: 412px; top: 86px; width: 392px; text-align: center; font-family: "Cinzel", serif; font-weight: 700; color: var(--tan); font-size: 48px; line-height: 46px; letter-spacing: 3px; }
  .year { position: absolute; left: 412px; top: 190px; width: 392px; text-align: center; font-family: "Josefin Sans", sans-serif; font-weight: 300; color: var(--tan-light); font-size: 50px; }
  .badge { position: absolute; left: 513px; top: 265px; width: 200px; height: 200px; }
  .facts { position: absolute; left: 0; top: 497px; width: 528px; list-style: none; }
  .facts li { color: var(--text); font-size: 24.5px; line-height: 32px; padding: 6px 0 16px 28px; border-bottom: 2px solid var(--tan); margin-bottom: 12px; }
  .facts li:last-child { border-bottom: none; }
  .contact { position: absolute; left: 29px; top: 1030px; color: var(--tan); font-size: 21.5px; line-height: 29px; }
  .photo-head { position: absolute; left: 563px; top: 806px; width: 286px; height: 394px; border-radius: 40% 30% 0 0 / 20% 15% 0 0; background: linear-gradient(160deg, var(--horse-mid) 0%, var(--horse-dark) 60%, #3a160a 100%); }
</style>
</head>
<body>
<main class="sheet">
  <svg class="sweep" width="849" height="1200" viewBox="0 0 849 1200" aria-hidden="true">
    <path d="M849 700 C 790 960, 580 1150, 190 1200 L849 1200 Z" fill="var(--tan)"/>
  </svg>

  <div class="title-frame"></div>
  <div class="photo-mount">
    <div class="photo-standing" role="img" aria-label="Photo of Northern Tempest, a bay stallion standing in profile in a stable yard"></div>
  </div>

  <h1 class="horse-name">NORTHERN TEMPEST</h1>
  <p class="year">2019</p>

  <svg class="badge" viewBox="0 0 200 200" aria-label="200 Winners">
    <defs>
      <radialGradient id="goldRing" cx="40%" cy="35%" r="70%">
        <stop offset="0" stop-color="#fff0a8"/>
        <stop offset="0.45" stop-color="var(--gold)"/>
        <stop offset="1" stop-color="var(--gold-dark)"/>
      </radialGradient>
    </defs>
    <circle cx="100" cy="100" r="97" fill="url(#goldRing)"/>
    <circle cx="100" cy="100" r="80" fill="var(--badge-core)" stroke="#8a6410" stroke-width="2"/>
    <text x="100" y="92" text-anchor="middle" font-family="Cabin, sans-serif" font-size="22" fill="var(--gold)">200</text>
    <text x="100" y="120" text-anchor="middle" font-family="Cabin, sans-serif" font-size="22" fill="var(--gold)">Winners</text>
  </svg>

  <ul class="facts">
    <li>Son of Distant Harbor with total progeny earnings over 13 million dollars</li>
    <li>Ranks among West Virginia top 3 active sires by progeny earnings 2019</li>
    <li>In 9 crops of racing age, has sired 200 winners from 275 starters</li>
    <li>Sired Don Marbellino who earned over $800k racing from age 2 to 7</li>
    <li>Won 3 of 4 lifetime starts</li>
  </ul>

  <p class="contact">Stands at stud for $1000 at Ashgrove<br>Farm near Charles Town<br>Call Dwight Kessler - (304) 555-0193</p>

  <div class="photo-head" role="img" aria-label="Close-up photo of Northern Tempest's head and neck wearing a halter"></div>
</main>
</body>
</html>
```